Can you make FairlyNeat look better than average? We need business cards and a logo refresh :-)

REVISED BRIEF

PRIORITY

VECTOR LOGO

Create a vector version of our existing logo. The logo must not change from its current design, weight or font.

Deliverables

- Logo in blue (#2540BB)
- Logo in white (#FFFFFF)
- Logo in grey (#36454F)
- All logos on transparent background
- All logos in PNG & SVG formats. (SVG must NOT distort stroke width when resized)

BRAND MARK

Create a brand mark for use with the logo. This should be possible to used with the logo and on its own as a stand alone graphical device that represents the FAIRLYNEAT brand.

https://quellbrik.com/resources/glossary/what-is-a-brand-mark

Deliverables

- Brand Mark in blue (#2540BB)
- Brand Mark in white (#FFFFFF)
- Brand Mark in grey (#36454F)
- Brand Mark on transparent background
- Brand Mark in PNG & SVG formats. (SVG must NOT distort stroke width when resized)
- Logo combined with Brand Mark (colours and formats)
.

Business Card Layout

Create 2 layouts with the following details:-

Marcus Delaney
Co-Founder & Chief Product Officer

marcus@fairlyneat.nz
www.fairlyneat.nz
0279831465

Callum Ferris
Founder & CEO

hello@fairlyneat.nz
www.fairlyneat.nz
021 684 2590

DESIGN CONSIDERATIONS

Create versions with ‘Shaping Causes With Heart’ tag line incorporated within the design and without (maintain separation of logo from tag line)

- Create a version with and without the brand mark
- Keep it clean and simple but elevate the design with subtle design effects
- Consider use of raised spot gloss colour (this can be white on white for subtle or blue on blue or blue on white)
- Consider use of spot gloss colour (this can be white on white for subtle or blue on blue or blue on white)
- Consider use of letterpress indentation
- Ensure contact details are legible, use sans-serif font

PREVIOUS BRIEF

We need a business card design for our business FairlyNeat. We are a purpose driven brand and media agency that helps brands and charities plan and buy traditional media campaigns (TV, Radio, Print, Outdoor etc). We give a significant amount of the media booking fees we receive from media vendors to charity in the name of our clients. https://www.plinkwork.com/posts/wearefairlyneat_giveback-fairlyneat-shapingcauseswithheart-activity-5829170364418205731-Rtqe

Our strapline is 'Shaping Causes With Heart'.

We want to keep our logo design as it is but it does need tightening up and made into a proper vector image as it's been created from a font.

Our brand colour is #2540BB and we need to keep this.

Our brand is professional but human, warm and engaging and doesn't take itself too seriously.

Things We Need
- vectorisation and tidying up of existing logo
- We'd like you to think about how we can incorporate a brand mark with the logo to add another dimension to our brand
- business card layout and design
- we'll be using zentiprint.com to print the cards so please take a look at the options they have (spot gloss, foil, letterpress, square cards and even the backs of the cards can have a different design on every single card!
- potential opportunity for different famous quotes on the back or imagery or slight design differences
- we'd be open to the use of an emoji or emojiis as the brandmark or to be incorporated into the card designs
- we can have as many different design batches as we like for the backs of the cards

https://www.zentiprint.com/au/business-cards

We want to make an impact, we want to be seen as professional but fun, we want to be different.

Here's a press release of what we're about.

https://adwirely.co.nz/movings-shakings/fairlyneat-welcomes-marcus-delaney-as-co-founder/

Be bold, be different, there is no such thing as a bad idea. We're open to anything so please bring your best ideas and have fun with it! Go crazy if you like!
____________
Marcus Delaney
marcus@fairlyneat.nz
0279831465

Callum Ferris
Founder & CEO
hello@fairlyneat.nz
021 684 2590

Shaping Causes With Heart

________

These are the only details we MUST have on the cards, the rest is up to you. Just make sure you use all of your creativity but don't feel the need to crowd the card with too much, let it breathe as well.

In terms of font for the details, we'll leave that up to you, just ensure it's legible. Oh and please don't take any design inspiration from our website - that will be changing!

Please don't let the design and layout look cheap and tacky though. It needs to still feel premium but personable.

Thanks

Marcus

Many designs are changing the logo and this was NOT in the brief. We need a brand mark to complement the logo. We need to see the logo with and without the brand mark. We need to see the business card with both logo + brand mark and logo on its own We need to see the business card with and without the tagline 'Shaping Causes With Heart'

purpose driven Brand & Media Agency

Shaping Causes With Heart
Marcus Delaney, Co-Founder & Chief Product Officer, marcus@fairlyneat.nz fairlyneet.nz, 0279 831 465

Callum Ferris, Founder & CEO hello@fairlyneat.nz, fairlyneet.nz, 021 684 2590

Serif
Sans Serif

0054AA
0677BA
7BADD7
CADEEF
E8F1F8

• brand mark, vector version of existing logo, Shaping Causes With Heart tagline, existing logo traced and vectorised. Must fully explore the design options from zentiprint.com that can enhance the overall card design
• brandmark to help elevate the logo, maybe incorporate some other design elements into the card like lines, or grids.
• A cheap look and feel

```html
<!DOCTYPE html>
<html lang="en">
<head>
<meta charset="utf-8">
<title>FairlyNeat Business Cards</title>
<link rel="stylesheet" href="https://fonts.googleapis.com/css2?family=Montserrat:wght@300;400;700;800;900&display=swap">
<style>
  :root {
    --brand-blue: #2540BB;
    --card-white: #FFFFFF;
    --page-bg: #E9EBF0;
    --card-shadow: rgba(20, 30, 70, 0.18);
    --portrait-light: #C9D6EA;
    --portrait-mid: #5F86C4;
    --portrait-dark: #3A4F7E;
  }
  * { box-sizing: border-box; margin: 0; padding: 0; }
  html, body { width: 1200px; height: 900px; overflow: hidden; }
  body {
    background: var(--page-bg);
    font-family: "Montserrat", sans-serif;
    display: flex;
    flex-direction: column;
    align-items: center;
    justify-content: center;
    gap: 48px;
  }
  .card {
    width: 620px;
    height: 354px;
    border-radius: 18px;
    box-shadow: 0 10px 28px var(--card-shadow);
    position: relative;
    overflow: hidden;
  }

  /* Front */
  .card--front {
    background: var(--brand-blue);
    color: var(--card-white);
    display: flex;
    flex-direction: column;
    align-items: center;
    justify-content: center;
  }
  .wordmark {
    display: flex;
    align-items: center;
    gap: 14px;
    font-weight: 900;
    letter-spacing: 0.5px;
  }
  .wordmark__square {
    width: 0.7em;
    height: 0.7em;
    background: currentColor;
  }
  .card--front .wordmark { font-size: 50px; }
  .tagline {
    margin-top: 40px;
    font-size: 22px;
    font-weight: 400;
    letter-spacing: 0.5px;
  }

  /* Back */
  .card--back {
    background: var(--card-white);
    color: var(--brand-blue);
  }
  .card--back .wordmark {
    position: absolute;
    left: 46px;
    top: 54px;
    font-size: 44px;
  }
  .person {
    position: absolute;
    left: 62px;
    top: 172px;
  }
  .person__name {
    font-size: 30px;
    font-weight: 800;
    line-height: 1.1;
  }
  .person__role {
    font-size: 15px;
    font-weight: 300;
    margin-top: 4px;
  }
  .contacts {
    list-style: none;
    margin-top: 22px;
    display: flex;
    flex-direction: column;
    gap: 8px;
  }
  .contacts__item {
    display: flex;
    align-items: center;
    gap: 12px;
    font-size: 15px;
    font-weight: 300;
  }
  .contacts__icon {
    width: 20px;
    height: 20px;
    border-radius: 5px;
    background: var(--brand-blue);
    display: flex;
    align-items: center;
    justify-content: center;
  }
  .portrait {
    position: absolute;
    right: 22px;
    top: 26px;
    width: 210px;
    height: 328px;
    border-radius: 105px 105px 0 0;
    background: linear-gradient(180deg, var(--portrait-light) 0%, var(--portrait-mid) 45%, var(--portrait-dark) 100%);
  }
</style>
</head>
<body>

  <section class="card card--front">
    <div class="wordmark">
      <span class="wordmark__square"></span>
      <span class="wordmark__name">FAIRLYNEAT</span>
    </div>
    <p class="tagline">Shaping Causes With Heart</p>
  </section>

  <section class="card card--back">
    <div class="wordmark">
      <span class="wordmark__name">FAIRLYNEAT</span>
    </div>

    <div class="person">
      <h1 class="person__name">Marcus Delaney</h1>
      <p class="person__role">Co-Founder &amp; Chief Product Officer</p>

      <ul class="contacts">
        <li class="contacts__item">
          <span class="contacts__icon">
            <svg width="12" height="12" viewBox="0 0 24 24" fill="none" stroke="#fff" stroke-width="2.4" stroke-linecap="round" stroke-linejoin="round">
              <path d="M22 16.9v3a2 2 0 0 1-2.2 2 19.8 19.8 0 0 1-8.6-3.1 19.5 19.5 0 0 1-6-6A19.8 19.8 0 0 1 2.1 4.2 2 2 0 0 1 4.1 2h3a2 2 0 0 1 2 1.7c.1 1 .4 1.9.7 2.8a2 2 0 0 1-.5 2.1L8 9.9a16 16 0 0 0 6 6l1.3-1.3a2 2 0 0 1 2.1-.4c.9.3 1.8.6 2.8.7a2 2 0 0 1 1.7 2z"/>
            </svg>
          </span>
          <span>0279 831 465</span>
        </li>
        <li class="contacts__item">
          <span class="contacts__icon">
            <svg width="12" height="12" viewBox="0 0 24 24" fill="none" stroke="#fff" stroke-width="2.2">
              <circle cx="12" cy="12" r="10"/>
              <path d="M2 12h20M12 2a15 15 0 0 1 0 20M12 2a15 15 0 0 0 0 20"/>
            </svg>
          </span>
          <span>fairlyneet.nz</span>
        </li>
        <li class="contacts__item">
          <span class="contacts__icon">
            <svg width="12" height="12" viewBox="0 0 24 24" fill="none" stroke="#fff" stroke-width="2.4" stroke-linejoin="round">
              <rect x="2" y="5" width="20" height="14" rx="1"/>
              <path d="M2 6l10 7 10-7"/>
            </svg>
          </span>
          <span>marcus@fairlyneat.nz</span>
        </li>
      </ul>
    </div>

    <div class="portrait" role="img" aria-label="Portrait photo of Marcus Delaney, seated, wearing a blue blazer"></div>
  </section>

</body>
</html>
```